Auto Dealership needs a exterior sign

We need a sign design for an exterior sign that measures 10 Ft wide and 4 ft tall. The sign needs to say, "Tarn Motors" in large lettering and the address," 718 North Birch Avenue Salina, Utah 84971 needs to be below the lettering "Tarn Motors" Also the lettering "Dealer #" needs to be in the sign somewhere, preferable a lower corner. We would like the theme of the sign to be graphics associated with the San Rafael Swell in Utah. I will upload a a few graphics. I would prefer a graphic of Delicate Arch in Arches nation Park to be in the background of the sign. Colors are Red, White, Black, Tan and possible Blue or Yellow.

Here are a couple more ideas for what I am looking for. Simple design, solid back ground blue or red.Please look at attachment for my ideas. I want something similar to the pic of the velmox sign. Matbe the same font. With the arch in tan or brown. Added Friday, May 27, 2016

Reason: Have not had time to review and send feedback.

Target Market(s)

Buyers of cars, trucks, Powersports, Recreational vehicles, Motorcycles

Industry/Entity Type

Automotive

Colors
f04a51
0355a3
fbed22
ffffff
cadf82

Requirements
Must have
• A Large Border, with large font lettering and the lettering must have an outline that highlights the wording with preferable a bubbly font. Here is the wording,
• "Tarn Motors"
• 718 North Birch Avenue
• Salina, Utah 84971
• Dealer# 435-218-5937
• Autos Powersports Recreation
Nice to have
• I really want to use a Graphic of Delicate Arch in Utah as a background Graphic that can be on the side or in the middle. preferable extra large in the middle with the wording in front of it. Possible a Dark Red Sign or a Dark Blue Sign. Most important is the contrast between the signage and the lettering. It needs to really stick out.

```html
<!DOCTYPE html>
<html lang="en">
<head>
<meta charset="utf-8">
<title>Tarn Motors – Exterior Sign</title>
<link rel="stylesheet" href="https://fonts.googleapis.com/css2?family=Open+Sans:wght@700;800&display=swap">
<style>
  :root {
    --rust: #8b3818;
    --rust-dark: #6e2a10;
    --rust-light: #9a4420;
    --tan-edge: #d9b89a;
    --silver: #e6e6e6;
    --silver-shade: #9c9c9c;
    --white: #ffffff;
    --ink: #2a0d04;
    --sky-top: #4a86d8;
    --sky-low: #9fc2e8;
    --horizon: #b07a5e;
    --rock: #d0612a;
    --rock-deep: #a8441a;
  }
  html, body {
    margin: 0;
    padding: 0;
    overflow: hidden;
    background: #ffffff;
  }
  .sign {
    position: relative;
    width: 1200px;
    height: 480px;
    overflow: hidden;
    background: var(--rust);
    font-family: "Open Sans", Arial, sans-serif;
    color: var(--white);
  }
  .sign-art {
    position: absolute;
    inset: 0;
  }
  .brand-name {
    position: absolute;
    left: 176px;
    top: 40px;
    margin: 0;
    font-size: 100px;
    font-weight: 700;
    line-height: 1;
    letter-spacing: 1px;
    color: var(--white);
    -webkit-text-stroke: 3px var(--ink);
    paint-order: stroke fill;
    text-shadow: 0 0 10px rgba(40, 10, 0, 0.9), 0 0 18px rgba(40, 10, 0, 0.7);
  }
  .address {
    position: absolute;
    margin: 0;
    font-size: 38px;
    font-weight: 700;
    line-height: 1;
    color: var(--white);
  }
  .address-street { left: 96px; top: 198px; }
  .address-city { left: 142px; top: 268px; }
  .services {
    position: absolute;
    left: 96px;
    top: 350px;
    margin: 0;
    font-size: 27px;
    font-weight: 700;
    line-height: 1;
    color: var(--tan-edge);
    word-spacing: 6px;
  }
  .dealer {
    position: absolute;
    left: 76px;
    top: 424px;
    margin: 0;
    font-size: 35px;
    font-weight: 700;
    line-height: 1;
    color: var(--white);
    word-spacing: 4px;
  }
  .dealer-label { margin-right: 28px; }
</style>
</head>
<body>
  <main class="sign">
    <svg class="sign-art" width="1200" height="480" viewBox="0 0 1200 480">
      <defs>
        <linearGradient id="landscape-fill" x1="0" y1="0" x2="0" y2="1">
          <stop offset="0" stop-color="var(--sky-top)"/>
          <stop offset="0.42" stop-color="var(--sky-low)"/>
          <stop offset="0.55" stop-color="var(--horizon)"/>
          <stop offset="0.68" stop-color="var(--rock-deep)"/>
          <stop offset="1" stop-color="var(--rock)"/>
        </linearGradient>
        <linearGradient id="ribbon-fill" x1="0" y1="0" x2="0" y2="1">
          <stop offset="0" stop-color="var(--rust-dark)"/>
          <stop offset="0.5" stop-color="var(--rust-light)"/>
          <stop offset="1" stop-color="var(--rust-dark)"/>
        </linearGradient>
        <linearGradient id="silver-fill" x1="0" y1="0" x2="1" y2="1">
          <stop offset="0" stop-color="var(--white)"/>
          <stop offset="1" stop-color="var(--silver-shade)"/>
        </linearGradient>
      </defs>

      <path class="scenic-edge" d="M722 0 Q640 140 600 300 Q580 400 566 480 L580 480 Q594 400 614 300 Q654 140 736 0 Z" fill="var(--tan-edge)"/>
      <path class="scenic-photo" role="img" aria-label="Photograph of Delicate Arch in red sandstone at sunset, snow-capped mountains and blue sky behind" d="M736 0 Q654 140 614 300 Q594 400 580 480 L1200 480 L1200 0 Z" fill="url(#landscape-fill)"/>

      <path class="ribbon" d="M76 38 L880 38 L880 160 L76 160 L118 99 Z" fill="url(#ribbon-fill)"/>
      <path class="ribbon-notch" d="M76 38 L98 38 L132 99 L98 160 L76 160 L112 99 Z" fill="url(#silver-fill)"/>
      <path class="ribbon-rule" d="M98 158 L920 158 L920 162 L98 162 Z" fill="var(--silver)"/>
    </svg>

    <h1 class="brand-name">Tarn Motors</h1>
    <p class="address address-street">718 North Birch Avenue</p>
    <p class="address address-city">Salina, Utah 84971</p>
    <p class="services">Autos Powersports Recreation</p>
    <p class="dealer"><span class="dealer-label">Dealer#</span>435-218-5937</p>
  </main>
</body>
</html>
```